Keystone Institute Logo & Business card

Keystone Institute - Professional ICT Training
business is a training center.
Logo and business card that have an ID.
bold publicity, distinct, and prestige image
"Ensure professional Success"
that will attract target customer to come and take a look. that will look prestige on certificate after graduation, that will serve as a business tool to attract Business and enterprise customer (let them send their staff for training)

Target Market(s)

young professionals, university students, youth building career in IT fields

Industry/Entity Type

Education

Contact Information for Business Card

Font styles to use
Sans Serif

Colors

Designer to choose colors to be used in the design.

Requirements
Must have
• Logo Identity
• uniqueness
Nice to have
• catch phrase or illustration
Should not have
• just use alphabet as logo.

```html
<!DOCTYPE html>
<html lang="en">
<head>
<meta charset="utf-8">
<title>Keystone Institute – Business Card</title>
<link rel="stylesheet" href="https://fonts.googleapis.com/css2?family=Cinzel:wght@700&family=Lato:wght@400;700;900&display=swap">
<style>
  :root {
    --backdrop: #2a2a2a;
    --card-white: #ffffff;
    --navy: #1b4a80;
    --navy-deep: #19467c;
    --lime: #8cc63f;
    --ink: #2b2b2b;
    --rule: #9a9a9a;
  }
  * { margin: 0; padding: 0; box-sizing: border-box; }
  html, body { width: 1200px; height: 1200px; overflow: hidden; }
  body {
    background: var(--backdrop);
    position: relative;
    font-family: "Lato", sans-serif;
  }
  .card {
    position: absolute;
    top: 310px;
    height: 594px;
    overflow: hidden;
    box-shadow: 2px 3px 6px rgba(0,0,0,.6);
  }
  .card-front { left: 234px; width: 364px; background: var(--card-white); text-align: center; }
  .card-back { left: 627px; width: 369px; background: var(--navy-deep); text-align: center; }

  .brand-mark {
    position: absolute;
    left: 50%;
    top: 90px;
    width: 130px;
    height: 130px;
    margin-left: -65px;
    border-radius: 50%;
    border: 3px solid var(--lime);
  }
  .brand-name {
    position: absolute;
    left: 0; right: 0;
    font-family: "Cinzel", serif;
    font-weight: 700;
    color: var(--navy);
    letter-spacing: .5px;
  }
  .card-front .brand-name { top: 238px; font-size: 24px; }

  .holder-name {
    position: absolute; left: 0; right: 0; top: 334px;
    font-family: "Cinzel", serif; font-weight: 700;
    font-size: 22px; color: var(--navy);
  }
  .holder-role {
    position: absolute; left: 0; right: 0; top: 360px;
    font-size: 16px; color: var(--ink);
  }
  .icon-row {
    position: absolute; left: 87px; top: 395px; width: 190px; height: 24px;
  }
  .contact {
    position: absolute; left: 0; right: 0; top: 431px;
    font-size: 16px; line-height: 22px; color: var(--ink);
  }
  .divider {
    position: absolute; left: 88px; width: 195px; top: 506px;
    border-top: 1px solid var(--rule);
  }
  .address {
    position: absolute; left: 0; right: 0; top: 517px;
    font-size: 17px; line-height: 22px; color: var(--ink);
  }

  .back-mark {
    position: absolute; left: -10px; top: 40px;
    width: 350px; height: 390px;
    border-radius: 50%;
    border: 6px solid rgba(255,255,255,.08);
  }
  .card-back .brand-name {
    top: 468px; font-size: 30px; color: #ffffff;
  }
  .tagline {
    position: absolute; left: 0; right: 0; top: 524px;
    font-weight: 900; font-size: 16px; color: var(--lime);
    text-transform: uppercase; letter-spacing: .2px;
  }
</style>
</head>
<body>
  <section class="card card-front">
    <div class="brand-mark"></div>
    <div class="brand-name">Keystone Institute</div>

    <div class="holder-name">Daniel Hayes</div>
    <div class="holder-role">Managing Director</div>

    <svg class="icon-row" viewBox="0 0 190 24" aria-hidden="true">
      <line x1="0" y1="12" x2="52" y2="12" stroke="#9a9a9a" stroke-width="1.5"/>
      <line x1="138" y1="12" x2="190" y2="12" stroke="#9a9a9a" stroke-width="1.5"/>
      <circle cx="67" cy="12" r="12" fill="#8cc63f"/>
      <path d="M60 9 q7 -5 14 0 l-2 2 h-2 l-1 -2 h-4 l-1 2 h-2 z M61 12 h12 v5 h-12 z" fill="#fff"/>
      <circle cx="95" cy="12" r="12" fill="#8cc63f"/>
      <rect x="88" y="7" width="14" height="10" fill="none" stroke="#fff" stroke-width="1.6"/>
      <path d="M88 7 l7 6 l7 -6" fill="none" stroke="#fff" stroke-width="1.6"/>
      <circle cx="123" cy="12" r="12" fill="#8cc63f"/>
    </svg>

    <div class="contact">
      555 201 4870<br>
      info@keystoneinstitute.com<br>
      keystoneinstitute.net/connect
    </div>
    <div class="divider"></div>
    <div class="address">
      421, Address line here,<br>
      45452,Country Name
    </div>
  </section>

  <section class="card card-back">
    <div class="back-mark"></div>
    <div class="brand-name">Keystone Institute</div>
    <div class="tagline">Ensure Professional Success</div>
  </section>
</body>
</html>
```